Customs House descriptive business cards

We require a two-sided business card that has a simple yet elegant design. We want to be able to promote our services as a customs house. This card should include our logo, contact info and services offered with the logo being on one side and the contact info and services on the flip side

Target Market(s)

Importers / exporters to and from the Bahamas

Industry/Entity Type

Logistics

Contact Information for Business Card

The front side of the card could have the logo and the flip side should have the other relevant info

Font styles to use
Serif

Colors

Designer to choose colors to be used in the design.

Requirements
Must have
• (Kelpway Brokers Ltd) Logo, address and contact info also services:
• import customs clearance, Delivery & HAndling services,Florida pickups, Export packing & Crating Services, export customs clearance, Consulting

```html
<!DOCTYPE html>
<html lang="en">
<head>
<meta charset="utf-8">
<title>Kelpway Brokers Ltd – Business Cards</title>
<link rel="stylesheet" href="https://fonts.googleapis.com/css2?family=Libre+Baskerville:wght@400;700&display=swap">
<style>
  :root {
    --page-bg: #2b2d31;
    --card-bg: #1d2024;
    --blue: #1e7fd6;
    --blue-light: #3a9cf0;
    --silver: #b9bcc1;
    --rule: #34414f;
    --band-text: #0f1a26;
  }
  * { box-sizing: border-box; margin: 0; padding: 0; }
  html, body {
    width: 1200px; height: 800px; overflow: hidden;
    background: var(--page-bg);
    font-family: "Libre Baskerville", "Times New Roman", serif;
  }
  .canvas {
    width: 1200px; height: 800px;
    display: flex; flex-direction: column; align-items: center; justify-content: center; gap: 36px;
  }
  .card {
    position: relative;
    width: 620px; height: 354px;
    background: var(--card-bg);
    box-shadow: 0 14px 30px rgba(0,0,0,.45);
    overflow: hidden;
    display: flex;
  }
  .brand {
    width: 300px; height: 100%;
    display: flex; flex-direction: column; align-items: center; justify-content: center;
    gap: 10px;
  }
  .brand-mark {
    width: 44px; height: 44px; border-radius: 50%;
    background: var(--blue);
  }
  .brand-name {
    color: var(--blue);
    font-size: 30px; font-weight: 700; letter-spacing: 2px;
    text-align: center; line-height: 1.15;
  }
  .divider {
    width: 1px; background: var(--rule);
    margin: 40px 0;
  }
  .contact-side { padding: 52px 0 0 34px; }
  .contact-side .brand { height: calc(100% - 58px); }
  .contact-side .divider { margin-bottom: 98px; }
  .person-name {
    color: var(--blue); font-size: 19px; font-weight: 700; letter-spacing: 1px;
  }
  .person-title { color: var(--silver); font-size: 13px; margin: 4px 0 18px; }
  .contact-list { list-style: none; }
  .contact-list li {
    color: var(--silver); font-size: 13px;
    display: flex; align-items: center; gap: 10px; margin-bottom: 7px;
  }
  .contact-list li.web { color: var(--blue); padding-left: 22px; }
  .contact-list li.web .www { color: var(--silver); }
  .contact-list svg { width: 12px; height: 12px; fill: var(--blue); flex: none; }
  .address-band {
    position: absolute; left: 0; right: 0; bottom: 30px; height: 28px;
    background: linear-gradient(90deg, var(--blue) 0%, var(--blue-light) 100%);
    color: var(--band-text);
    font-size: 13px; font-weight: 700;
    display: flex; align-items: center; justify-content: center;
  }
  .contact-card { display: flex; }
  .contact-card .brand { height: 296px; }
  .contact-card .divider { margin: 40px 0 98px; }
  .contact-details { padding: 56px 0 0 34px; }
  .services { padding: 72px 0 0 34px; }
  .services-title {
    color: var(--blue); font-size: 19px; font-weight: 700; letter-spacing: 1px; margin-bottom: 18px;
  }
  .services-list { list-style: none; }
  .services-list li {
    color: var(--silver); font-size: 14px;
    display: flex; align-items: center; gap: 10px; margin-bottom: 8px;
  }
  .services-list li::before {
    content: ""; width: 7px; height: 7px; background: var(--blue);
    transform: rotate(45deg); flex: none;
  }
</style>
</head>
<body>
<main class="canvas">

  <section class="card contact-card">
    <div class="brand">
      <span class="brand-mark"></span>
      <span class="brand-name">KELPWAY<br>BROKERS LTD.</span>
    </div>
    <div class="divider"></div>
    <div class="contact-details">
      <h1 class="person-name">DARREN WHITFIELD</h1>
      <p class="person-title">Operations Director</p>
      <ul class="contact-list">
        <li>
          <svg viewBox="0 0 24 24" aria-hidden="true"><path d="M6.6 10.8a15.1 15.1 0 0 0 6.6 6.6l2.2-2.2c.3-.3.7-.4 1-.2 1.1.4 2.3.6 3.6.6.6 0 1 .4 1 1V20c0 .6-.4 1-1 1C10.6 21 3 13.4 3 4c0-.6.4-1 1-1h3.5c.6 0 1 .4 1 1 0 1.3.2 2.5.6 3.6.1.3 0 .7-.2 1z"/></svg>
          (242)555-0148
        </li>
        <li>
          <svg viewBox="0 0 24 24" aria-hidden="true"><path d="M7 2h10a2 2 0 0 1 2 2v16a2 2 0 0 1-2 2H7a2 2 0 0 1-2-2V4a2 2 0 0 1 2-2zm0 3v12h10V5z"/></svg>
          (242)555-0192
        </li>
        <li>
          <svg viewBox="0 0 24 24" aria-hidden="true"><path d="M2 5h20v14H2zm2 2v.5l8 5 8-5V7l-8 5z"/></svg>
          imports@kelpwaybrokers.com
        </li>
        <li class="web"><span><span class="www">www.</span>KELPWAYBROKERS.com</span></li>
      </ul>
    </div>
    <div class="address-band">#42 Coral Ridge Road, P.O. BOX SP-70215, Nassau, Bahamas</div>
  </section>

  <section class="card services-card">
    <div class="brand">
      <span class="brand-mark"></span>
      <span class="brand-name">KELPWAY<br>BROKERS LTD.</span>
    </div>
    <div class="divider"></div>
    <div class="services">
      <h2 class="services-title">OUR SERVICES</h2>
      <ul class="services-list">
        <li>import customs clearance</li>
        <li>Delivery &amp; HAndling services</li>
        <li>Florida pickups</li>
        <li>Export packing &amp; Crating Services</li>
        <li>export customs clearance</li>
        <li>Consulting</li>
      </ul>
    </div>
  </section>

</main>
</body>
</html>
```